Business Card for Ferncliff Massage

I need a business card for my massage therapy & cannabis oil practice. I already have a logo,the "massage" got edited out of this file. I will send the original soon. I need these elements to be on the card:
web: FerncliffMassage.example
ph: 417/283-9061
email: Mirela.Dawkant@mailbox.example
Other slogans, statements to consider:
Science Geek, Massage Therapist, Neuromuscular Therapy, Cannabis Spa Treatments, Raindrop Therapy, Essential Oils
Target Market(s)
women between 20 & 65, people with enough $ to afford regular massage, people who recently had a motor vehicle accident, Halvora HMP insured
Industry/Entity Type
Massage Therapy
Contact Information for Business Card
I would like to see my bear logo featured; contact details, greens & blues preferred colors.

```html
<!DOCTYPE html>
<html lang="en">
<head>
<meta charset="utf-8">
<title>Ferncliff Massage – Business Card</title>
<link rel="stylesheet" href="https://fonts.googleapis.com/css2?family=Libre+Baskerville:wght@400;700&display=swap">
<style>
  :root {
    --backdrop: #2b2b2b;
    --card: #ffffff;
    --green: #2f7d32;
    --stone: #9a8579;
    --stone-dark: #6f655d;
    --text: #6b5a4f;
    --serif: "Libre Baskerville", Georgia, serif;
  }
  * { box-sizing: border-box; margin: 0; padding: 0; }
  html, body { width: 1200px; height: 873px; overflow: hidden; }
  body { background: var(--backdrop); position: relative; font-family: var(--serif); }

  .card {
    position: absolute;
    width: 560px;
    height: 320px;
    background: var(--card);
    border-radius: 16px;
    overflow: hidden;
  }
  .card--back  { left: 50px;  top: 90px; }
  .card--front { left: 590px; top: 460px; }

  /* Back side */
  .services {
    position: absolute;
    left: 330px;
    top: 58px;
    list-style: none;
  }
  .services li {
    display: flex;
    align-items: center;
    gap: 10px;
    font-size: 13px;
    color: var(--text);
    line-height: 22px;
    white-space: nowrap;
  }
  .services .dot { width: 12px; height: 7px; border-radius: 50%; flex: none; }
  .dot--stone { background: var(--stone-dark); }
  .dot--green { background: var(--green); }
  .back-name {
    position: absolute;
    left: 36px;
    top: 214px;
    font-size: 46px;
    line-height: 1.2;
    font-weight: 400;
    color: var(--stone);
    display: flex;
    align-items: center;
    gap: 12px;
    white-space: nowrap;
  }
  .back-name .mark { width: 20px; height: 20px; border-radius: 50%; background: var(--green); flex: none; }

  /* Front side */
  .brand {
    position: absolute;
    left: 34px;
    top: 182px;
    display: flex;
    align-items: center;
    gap: 10px;
    font-size: 36px;
    line-height: 1.2;
    color: var(--green);
    white-space: nowrap;
  }
  .brand .mark { width: 14px; height: 14px; border-radius: 50%; background: var(--stone); flex: none; }
  .divider {
    position: absolute;
    left: 262px;
    top: 36px;
    width: 2px;
    height: 136px;
    background: var(--green);
  }
  .contact {
    position: absolute;
    left: 278px;
    top: 42px;
    color: var(--text);
    font-size: 12.5px;
    font-weight: 700;
    line-height: 19px;
    white-space: nowrap;
  }
  .contact address { font-style: normal; margin-bottom: 8px; }
  .contact ul { list-style: none; }
  .contact li { display: flex; align-items: center; gap: 9px; font-weight: 400; }
  .contact svg { width: 12px; height: 12px; flex: none; fill: var(--text); }
  .swoosh { position: absolute; left: 0; top: 0; }
</style>
</head>
<body>

<section class="card card--back" aria-label="Card back">
  <ul class="services">
    <li><span class="dot dot--stone"></span>Science Geek</li>
    <li><span class="dot dot--green"></span>Massage Therapist</li>
    <li><span class="dot dot--stone"></span>Neuromuscular Therapy</li>
    <li><span class="dot dot--stone"></span>Cannabis Spa Treatments</li>
    <li><span class="dot dot--green"></span>Raindrop Therapy</li>
    <li><span class="dot dot--stone"></span>Essential Oils</li>
  </ul>
  <p class="back-name"><span class="mark"></span>Ferncliff</p>
</section>

<section class="card card--front" aria-label="Card front">
  <svg class="swoosh" width="560" height="320" viewBox="0 0 560 320" aria-hidden="true">
    <path d="M0 262 C180 254 360 232 470 204 C380 246 200 272 0 279 Z" fill="var(--stone)"/>
    <path d="M0 286 C200 276 420 236 560 172 L560 320 L0 320 Z" fill="var(--green)"/>
  </svg>

  <p class="brand">Ferncliff<span class="mark"></span></p>
  <span class="divider"></span>

  <div class="contact">
    <address>7/41 Larkmoor Ave<br>Dunmere Flats QLD 4190</address>
    <ul>
      <li>
        <svg viewBox="0 0 24 24"><path d="M6.6 10.8a15.2 15.2 0 0 0 6.6 6.6l2.2-2.2a1 1 0 0 1 1-.25 11.4 11.4 0 0 0 3.6.57 1 1 0 0 1 1 1V20a1 1 0 0 1-1 1A17 17 0 0 1 3 4a1 1 0 0 1 1-1h3.5a1 1 0 0 1 1 1c0 1.25.2 2.45.57 3.6a1 1 0 0 1-.25 1z"/></svg>
        417/283-9061
      </li>
      <li>
        <svg viewBox="0 0 24 24"><path d="M2 5h20v14H2z M2 5l10 8 10-8" fill="none" stroke="#6b5a4f" stroke-width="2"/></svg>
        Mirela.Dawkant@mailbox.example
      </li>
      <li>
        <svg viewBox="0 0 24 24"><circle cx="12" cy="12" r="10" fill="none" stroke="#6b5a4f" stroke-width="2"/><path d="M2 12h20M12 2c3 3 3 17 0 20M12 2c-3 3-3 17 0 20" fill="none" stroke="#6b5a4f" stroke-width="1.6"/></svg>
        www.FerncliffMassage.example
      </li>
    </ul>
  </div>
</section>

</body>
</html>
```